SilverLedgerOak - Double Sided Business Card

We are looking for design options or our business cards. We are a Business Solutions and HR solutions Provider - the theme is business, for this card.

Our brand colours are represented within our logo.

Details needed to be put on the front of the business card are:

Employees name: [Sample Name]
Role: [Sample Role]

Address: Suite 4 - Level 3/48 Halloran Avenue Parramatta NSW 2150
M: 0000 000 000
P: 1300 847 213
F: 1300 847 286
E: sample@silverledgeroak.com.au
www.silverledgeroak.com.au
Updates

Reason: Hello, could we please increase our deadline by 5 days. Thanking you, Tess

Target Market(s)

Business Owners, also Candidates looking for Employment

Industry/Entity Type

Business

Contact Information for Business Card

Role: [Sample Role]

M: 0000 000 000
P: 1300 847 213
F: 1300 847 286

Font styles to use
Sans Serif

Colors
3276b5
3176b5
0455a3
85abd2
cfdeed
ffffff
000000
1b1b1b
757575

Requirements
Must have
• Details needed to be put on the front of the business card are:
• Employees name: [Sample Name]
• Role: [Sample Role]
• Address: Suite 4 - Level 3/48 Halloran Avenue Parramatta NSW 2150
• M: 0000 000 000
• P: 1300 847 213
• F: 1300 847 286
• E: sample@silverledgeroak.com.au
• www.silverledgeroak.com.au
Nice to have
• Simplicity, clean and professional.

```html
<!DOCTYPE html>
<html lang="en">
<head>
<meta charset="utf-8">
<title>SilverLedgerOak – Business Card</title>
<link href="https://fonts.googleapis.com/css2?family=Oswald:wght@500&family=Questrial&display=swap" rel="stylesheet">
<style>
  :root {
    --navy: #13294b;
    --blue: #0c55a3;
    --ink: #1b1b1b;
    --paper: #ffffff;
    --edge: #9a9a9a;
  }
  html, body {
    margin: 0;
    padding: 0;
    width: 1200px;
    height: 1200px;
    overflow: hidden;
    background: var(--paper);
  }
  .canvas {
    position: relative;
    width: 1200px;
    height: 1200px;
  }
  .card {
    position: absolute;
    left: 196px;
    width: 809px;
    height: 462px;
    box-sizing: border-box;
    overflow: hidden;
  }
  .card--front {
    top: 107px;
    border: 1px solid var(--edge);
    background: var(--paper);
  }
  .card--back {
    top: 600px;
    background: linear-gradient(135deg, var(--navy) 0%, var(--blue) 50%, var(--navy) 100%);
  }
  .edge-motif {
    position: absolute;
    width: 94px;
    height: 220px;
  }
  .edge-motif--left {
    left: 0;
    top: 120px;
    background: linear-gradient(180deg, var(--navy), #1f3a66);
  }
  .edge-motif--right {
    right: 0;
    top: 108px;
    background: linear-gradient(180deg, var(--navy), var(--blue));
  }
  .accent-rule {
    position: absolute;
    left: 342px;
    top: 82px;
    width: 124px;
    height: 3px;
    background: var(--blue);
  }
  .name {
    position: absolute;
    left: 0;
    right: 0;
    top: 100px;
    margin: 0;
    text-align: center;
    font-family: "Oswald", sans-serif;
    font-weight: 500;
    font-size: 40px;
    line-height: 50px;
    letter-spacing: 0.1em;
    color: var(--blue);
  }
  .role {
    position: absolute;
    left: 0;
    right: 0;
    top: 157px;
    margin: 0;
    text-align: center;
    font-family: "Questrial", sans-serif;
    font-size: 20px;
    line-height: 26px;
    letter-spacing: 0.2em;
    color: var(--navy);
  }
  .details {
    position: absolute;
    left: 0;
    right: 0;
    top: 200px;
    margin: 0;
    padding: 0;
    list-style: none;
    text-align: center;
    font-family: "Questrial", sans-serif;
    font-size: 16.5px;
    letter-spacing: 0.08em;
    color: var(--ink);
  }
  .details li {
    height: 29px;
    line-height: 20px;
  }
  .details li.web {
    margin-top: 3px;
  }
</style>
</head>
<body>
<main class="canvas">
  <section class="card card--front" aria-label="Business card front">
    <div class="edge-motif edge-motif--left" role="img" aria-label="Brand geometric motif cropped at card edge"></div>
    <div class="edge-motif edge-motif--right" role="img" aria-label="Brand geometric motif cropped at card edge"></div>
    <div class="accent-rule"></div>
    <h1 class="name">DANIEL REEVES</h1>
    <p class="role">administrative assistant</p>
    <ul class="details">
      <li>Suite 4 - Level 3/48 Halloran Avenue</li>
      <li>Parramatta, NSW</li>
      <li>[m] 0000 000 000</li>
      <li>[p] 1300 847 213</li>
      <li>[f] 1300 847 286</li>
      <li>daniel@silverledgeroak.com.au</li>
      <li class="web">silverledgeroak.com.au</li>
    </ul>
  </section>
  <section class="card card--back" role="img" aria-label="Repeating brand pattern in navy and blue covering the card back"></section>
</main>
</body>
</html>
```